Kelvo Auto - help to get me noticed

We not long ago tasked Pixel Harbour to design a logo for my business. I'm happy with the result so would like to have a business card designed as a follow up.

It's an Automotive service and repair business that offers the following -
- Servicing
- General repairs
- Brakes
- Detailing
- Integrity

Kelvo Automotive
Dallin Mereth
0471 926 317

Target Market(s)

Everyday people with the ability to reach out to corporate customers also.

Industry/Entity Type

Automotive

Contact Information for Business Card

Black card, logo, name and phone number on front. Other details on back of card.

```html
<!DOCTYPE html>
<html lang="en">
<head>
<meta charset="utf-8">
<title>Kelvo Automotive – Business Card</title>
<link href="https://fonts.googleapis.com/css2?family=Russo+One&family=Saira:wght@700&family=Montserrat:wght@400;500&display=swap" rel="stylesheet">
<style>
  :root{
    --page:#d9d9d7;
    --card:#161616;
    --green:#7cc242;
    --green-mid:#3da34a;
    --green-dark:#1e4a26;
    --white:#ffffff;
  }
  *{margin:0;padding:0;box-sizing:border-box}
  html,body{width:1200px;height:1200px;overflow:hidden;background:var(--page)}
  .sheet{position:relative;width:1200px;height:1200px;display:flex;flex-direction:column;align-items:center;justify-content:center;gap:56px}
  .card{position:relative;width:900px;height:514px;background:var(--card);overflow:hidden;box-shadow:0 10px 30px rgba(0,0,0,.25)}
  .card svg{position:absolute;inset:0;width:100%;height:100%}

  /* back side */
  .brand{font-family:"Russo One",sans-serif;color:var(--green);line-height:1;text-transform:uppercase}
  .back .brand{position:absolute;left:0;right:0;top:150px;text-align:center}
  .brand-main{display:block;font-size:88px;letter-spacing:2px}
  .brand-sub{display:block;font-size:34px;letter-spacing:9px;margin-top:8px}
  .services{position:absolute;left:0;right:0;top:330px;text-align:center;font-family:"Saira",sans-serif;font-weight:700;font-size:22px;letter-spacing:3px;color:var(--green);text-transform:uppercase}
  .services .sep{margin:0 14px}

  /* front side */
  .front .brand{position:absolute;left:70px;top:70px}
  .front .brand-main{font-size:66px}
  .front .brand-sub{font-size:25px;letter-spacing:7px;margin-top:6px}
  .contact{position:absolute;left:70px;top:262px;font-family:"Montserrat",sans-serif;color:var(--white)}
  .contact-name{font-size:30px;font-weight:500;letter-spacing:2px;text-transform:uppercase}
  .contact-phone{font-size:20px;font-weight:400;letter-spacing:1.5px;margin-top:14px}
</style>
</head>
<body>
<main class="sheet">

  <section class="card back" aria-label="Business card back">
    <svg viewBox="0 0 900 514" preserveAspectRatio="none">
      <defs>
        <radialGradient id="carGlow" cx="50%" cy="55%" r="50%">
          <stop offset="0" stop-color="#262626"/>
          <stop offset="1" stop-color="#161616" stop-opacity="0"/>
        </radialGradient>
      </defs>
      <rect role="img" aria-label="Faint silhouette of a sports car behind the logo" x="60" y="120" width="800" height="320" fill="url(#carGlow)"/>
    </svg>
    <div class="brand">
      <span class="brand-main">Kelvo</span>
      <span class="brand-sub">Automotive</span>
    </div>
    <p class="services">Servicing<span class="sep">-</span>General Repairs<span class="sep">-</span>Brakes<span class="sep">-</span>Detailing<span class="sep">-</span>Integrity</p>
  </section>

  <section class="card front" aria-label="Business card front">
    <svg viewBox="0 0 900 514" preserveAspectRatio="none">
      <defs>
        <linearGradient id="interior" x1="0" y1="0" x2="1" y2="1">
          <stop offset="0" stop-color="#c9ccce"/>
          <stop offset=".35" stop-color="#4a4f55"/>
          <stop offset=".7" stop-color="#23272b"/>
          <stop offset="1" stop-color="#15181b"/>
        </linearGradient>
      </defs>
      <path class="band-dark" d="M505 0 Q335 200 245 514 L335 514 Q405 190 565 0 Z" fill="var(--green-dark)"/>
      <path class="band-line" d="M548 0 Q390 195 316 514" fill="none" stroke="var(--green-mid)" stroke-width="10"/>
      <path class="band-light" d="M566 0 Q405 192 334 514" fill="none" stroke="var(--green)" stroke-width="16"/>
      <path role="img" aria-label="Photo of a car interior with steering wheel and dashboard" d="M578 0 L900 0 L900 514 L346 514 Q418 190 578 0 Z" fill="url(#interior)"/>
    </svg>
    <div class="brand">
      <span class="brand-main">Kelvo</span>
      <span class="brand-sub">Automotive</span>
    </div>
    <div class="contact">
      <p class="contact-name">Dallin Mereth</p>
      <p class="contact-phone">M: 0471 926 317</p>
    </div>
  </section>

</main>
</body>
</html>
```